Luxury Business Card Design for High-End Window Treatments

Gilded Vantages
Custom Plantation Shutters & Architectural Shading Systems

⸻

BACK

Daniel Forsythe
Owner

Custom Interior & Exterior Window Treatments

919-482-7034
gildedvantages.com

I have included a picture that I’m hoping we can use on the back, but I’m also wondering if you can get rid of the ladder? Should we get rid of shutters , shades and blinds underneath Gilded Vantages?

Target Market(s)

High-end residential homeowners, custom home builders, architects, interior designers, and luxury renovation clients seeking premium plantation shutters and motorized architectural shading systems.

Industry/Entity Type

Custom Window treatments

Contact Information for Business Card

Front Gilded Vantages Custom Plantation Shutters Motorized Architectural Shading Systems BACK Daniel Forsythe Owner 919-482-7034 GildedVantages.com Custom Interior & Exterior Window Treatments By Appointment

Requirements
Nice to have
• Not 100% sure on nice to halves or the color but you can definitely check out my website to get a better understanding of what I’m trying to do

```html
<!DOCTYPE html>
<html lang="en">
<head>
<meta charset="utf-8">
<title>Gilded Vantages Business Card</title>
<link href="https://fonts.googleapis.com/css2?family=Poppins:wght@400;500;600&display=swap" rel="stylesheet">
<style>
  :root {
    --stage: #ababab;
    --cream: #e6dfd1;
    --ink: #2b2b2b;
    --ink-soft: #4a4a4a;
    --gold: #d3b24a;
    --night-top: #2a2e36;
    --night-bottom: #1b1d22;
    --white: #ffffff;
  }
  * { box-sizing: border-box; margin: 0; padding: 0; }
  html, body { width: 1200px; height: 240px; overflow: hidden; }
  body {
    background: var(--stage);
    font-family: "Poppins", sans-serif;
    position: relative;
  }
  .card {
    position: absolute;
    top: 29px;
    width: 320px;
    height: 182px;
    border-radius: 40px;
    overflow: hidden;
  }
  .card--front { left: 250px; background: var(--cream); color: var(--ink); }
  .card--back { left: 630px; background: var(--night-bottom); color: var(--white); }
  .gold-band {
    position: absolute; left: 0; right: 0; bottom: 0;
    height: 5px; background: var(--gold);
  }
  .brand {
    position: absolute; left: 211px; top: 20px;
  }
  .brand__name {
    display: flex; align-items: center; gap: 4px;
    font-size: 10.5px; font-weight: 500; line-height: 1.1;
  }
  .brand__dot {
    width: 6px; height: 6px; border-radius: 50%; background: var(--ink);
  }
  .brand__services {
    margin-top: 5px;
    font-size: 4.6px; font-weight: 500; word-spacing: 3px;
  }
  .contact { position: absolute; left: 211px; top: 103px; }
  .contact__name { font-size: 10.2px; font-weight: 600; }
  .contact__role { font-size: 5.4px; color: var(--ink-soft); margin-top: 2px; }
  .contact__service { font-size: 4.9px; font-weight: 500; margin-top: 6px; line-height: 1.3; }
  .contact__lines { margin-top: 6px; list-style: none; font-size: 5.2px; font-weight: 500; line-height: 1.3; }
  .contact__lines li { display: flex; align-items: center; gap: 5px; }
  .contact__lines svg { width: 5px; height: 5px; }
  .back-photo {
    position: absolute; inset: 0;
    background: linear-gradient(180deg, #3a4150 0%, var(--night-top) 35%, #23262c 70%, #2f2a24 100%);
  }
  .back-photo::after {
    content: ""; position: absolute; inset: 0; background: rgba(20, 20, 24, 0.45);
  }
  .back-content {
    position: absolute; inset: 0;
    display: flex; flex-direction: column; align-items: center;
  }
  .back-content__name {
    margin-top: 55px; display: flex; align-items: center; gap: 6px;
    font-size: 18px; font-weight: 400; letter-spacing: 0.2px;
  }
  .back-content__dot { width: 8px; height: 8px; border-radius: 50%; background: var(--white); }
  .back-content__tagline {
    margin-top: 24px; text-align: center;
    font-size: 7.2px; line-height: 1.25;
  }
</style>
</head>
<body>
  <section class="card card--front">
    <div class="brand">
      <div class="brand__name"><span class="brand__dot"></span>Gilded Vantages</div>
      <div class="brand__services">Shutters Shades Blinds</div>
    </div>
    <div class="contact">
      <div class="contact__name">Daniel Forsythe</div>
      <div class="contact__role">Owner</div>
      <div class="contact__service">Custom Interior &amp;<br>Exterior Window Treatments</div>
      <ul class="contact__lines">
        <li>
          <svg viewBox="0 0 10 10"><path d="M2 1l2 0 1 2.5-1.3 1a5 5 0 0 0 2.8 2.8l1-1.3L10 7v2c0 .6-.4 1-1 1A9 9 0 0 1 0 2c0-.6.4-1 1-1z" fill="currentColor"/></svg>
          919-482-7034
        </li>
        <li>
          <svg viewBox="0 0 10 10"><circle cx="5" cy="5" r="4.3" fill="none" stroke="currentColor" stroke-width="1"/><path d="M.7 5h8.6M5 .7c-2.4 2.6-2.4 6 0 8.6M5 .7c2.4 2.6 2.4 6 0 8.6" fill="none" stroke="currentColor" stroke-width=".8"/></svg>
          gildedvantages.com
        </li>
      </ul>
    </div>
    <div class="gold-band"></div>
  </section>

  <section class="card card--back">
    <div class="back-photo" role="img" aria-label="Evening photograph of a home's screened porch with white columns and trees"></div>
    <div class="back-content">
      <div class="back-content__name"><span class="back-content__dot"></span>Gilded Vantages</div>
      <p class="back-content__tagline">Custom Plantation Shutters &amp; Architectural<br>Shading Systems</p>
    </div>
    <div class="gold-band"></div>
  </section>
</body>
</html>
```